Golf Day Flyer - Hartwell School

Flyer for a golf day.
Parents and friends of a school are invited to play golf on Monday 22nd October.

Flyer from last year (2017) is attached. We would like to make the flyer more fun/humorous this year.

The golf day has two sessions: (1) Round of golf starting at 9AM and (2) Golf Clinic for beginner golfers.

So the flyer could have two sections - one showing experienced golfers, the other showing beginner golfers.

We have not finalised all the content for the flyer yet but need to look at some designs before we give all the content.

Target Market(s)

parents and friends of the school students - professionals (accountants, lawyers, doctors, etc)

Industry/Entity Type

Golf Course

Font styles to use
Serif

Colors

Designer to choose colors to be used in the design.

Requirements
Must have
• Refer to content attached document
Nice to have
• Funny golf pictures
Should not have
• N/A

```html
<!DOCTYPE html>
<html lang="en">
<head>
<meta charset="utf-8">
<title>Hartwell Golf Day 2018</title>
<link rel="stylesheet" href="https://fonts.googleapis.com/css2?family=Oswald:wght@500;700&family=Roboto+Condensed:ital,wght@0,400;0,700;0,800;1,700&family=Roboto+Slab:wght@400;600&family=Roboto:wght@300;400&display=swap">
<style>
  :root {
    --page: #3a3a3a;
    --paper: #ffffff;
    --grass-dark: #2f6a12;
    --grass: #4f8f1f;
    --grass-light: #7fb53a;
    --brand-green: #169a1f;
    --hot-pink: #f0245a;
    --sun-yellow: #f4f00c;
    --ink: #0c0c0c;
    --white: #ffffff;
  }
  * { box-sizing: border-box; margin: 0; padding: 0; }
  html, body { width: 1200px; height: 1200px; overflow: hidden; background: var(--page); }

  .flyer {
    position: absolute; left: 152px; top: 20px;
    width: 896px; height: 1160px;
    background: var(--paper);
    overflow: hidden;
  }
  .grass-field {
    position: absolute; left: 17px; top: 17px; width: 862px; height: 1123px;
    background:
      radial-gradient(ellipse at 95% 70%, rgba(240,36,90,.55), transparent 30%),
      radial-gradient(ellipse at 5% 75%, rgba(240,36,90,.6), transparent 22%),
      radial-gradient(ellipse at 90% 3%, rgba(240,36,90,.45), transparent 25%),
      linear-gradient(160deg, var(--grass-light), var(--grass) 40%, var(--grass-dark));
  }
  .spotlight {
    position: absolute; left: 108px; top: 90px; width: 680px; height: 680px;
    border-radius: 50%;
    background: radial-gradient(circle, var(--white) 0 62%, rgba(255,255,255,.75) 70%, rgba(255,255,255,0) 80%);
  }

  .date-band {
    position: absolute; left: 106px; top: 165px; width: 619px; height: 90px;
    background: var(--hot-pink); border-radius: 45px 20px 30px 50px;
    transform: rotate(-3deg);
    display: flex; align-items: center; justify-content: center;
  }
  .date-band span {
    font: 700 54px/1 "Oswald", sans-serif; color: var(--ink);
    text-shadow: 3px 3px 0 var(--sun-yellow); letter-spacing: -1px;
    white-space: nowrap;
    transform: scaleX(.85); padding-left: 60px;
  }

  .title {
    position: absolute; left: 245px; top: 0; width: 420px; height: 580px;
    font-family: "Roboto Condensed", sans-serif; font-weight: 800;
    line-height: 1; white-space: nowrap;
  }
  .title span { position: absolute; left: 0; display: block; }
  .title .name { top: 240px; color: var(--brand-green); font-size: 88px; letter-spacing: -1px; }
  .title .golf { top: 295px; color: var(--ink); font-size: 190px; letter-spacing: -2px;
    text-shadow: 4px 4px 0 var(--sun-yellow); }
  .title .year { top: 448px; color: var(--brand-green); font-size: 105px; letter-spacing: -2px; }

  .location { position: absolute; left: 20px; right: 0; top: 591px; text-align: center; }
  .location .label {
    font: 300 31px/1 "Roboto", sans-serif; letter-spacing: 9px; color: var(--ink);
    display: inline-flex; align-items: center; gap: 4px; white-space: nowrap;
  }
  .location .venue {
    position: absolute; left: 0; right: 0; top: 28px;
    font: 700 36px/1 "Roboto Condensed", sans-serif; color: var(--hot-pink); white-space: nowrap;
  }

  .start-band {
    position: absolute; left: 89px; top: 693px; width: 721px; height: 69px;
    background: var(--sun-yellow); border-radius: 35px;
    transform: rotate(-.5deg);
    display: flex; align-items: center; justify-content: center;
  }
  .start-band span {
    font: italic 700 34px/1 "Roboto Condensed", sans-serif; color: var(--ink);
    letter-spacing: -.5px; white-space: nowrap; transform: scaleX(.76);
  }

  .sessions {
    position: absolute; top: 783px; left: 0; width: 100%;
    font-family: "Roboto Slab", serif; color: var(--white);
    text-shadow: 0 1px 3px rgba(0,0,0,.6);
  }
  .session { position: absolute; white-space: nowrap; }
  .session h3 { font-weight: 400; font-size: 26px; line-height: 1; margin-bottom: 6px; letter-spacing: -.5px; }
  .session p { font-size: 16px; line-height: 21px; font-weight: 600; }
  .session--clinic { right: 475px; text-align: right; }
  .session--lunch { left: 440px; }

  .golf-ball {
    position: absolute; left: 29px; top: 895px; width: 218px; height: 202px;
    border-radius: 50%;
    background: radial-gradient(circle at 55% 40%, #f2f4fa, #b9c2d6 60%, #7d8aa6);
  }

  .payment { position: absolute; left: 275px; top: 977px; height: 48px; display: flex; align-items: center; }
  .payment .label {
    height: 48px; width: 174px; padding-left: 19px; background: var(--white); border-radius: 24px 0 0 24px;
    font: 700 31px/48px "Roboto Condensed", sans-serif; color: var(--ink); white-space: nowrap;
  }
  .payment .link {
    height: 48px; width: 403px; margin-left: -13px; padding-left: 32px;
    background: var(--hot-pink); border-radius: 24px;
    font: 400 30px/48px "Roboto Condensed", sans-serif; color: var(--white);
    position: relative; white-space: nowrap;
  }
  .payment .cursor { position: absolute; left: 10px; top: 20px; }
  .pricing {
    position: absolute; right: 86px; top: 1035px;
    font: 700 15px/1 "Roboto Condensed", sans-serif; color: var(--white);
  }
  .function-band {
    position: absolute; left: 215px; top: 1077px; width: 560px; height: 23px;
    padding-right: 30px;
    background: linear-gradient(90deg, rgba(0,0,0,0), var(--ink) 10%, var(--ink) 80%, rgba(0,0,0,0));
    display: flex; align-items: center; justify-content: center;
    font: 400 16px/1 "Roboto Condensed", sans-serif; color: var(--white); white-space: nowrap;
  }
</style>
</head>
<body>
<main class="flyer">
  <div class="grass-field" role="img" aria-label="Close-up photograph of golf course grass with pink and white halftone splashes"></div>
  <div class="spotlight"></div>

  <div class="date-band"><span>22ND | MON | OCT | 2018</span></div>

  <h1 class="title">
    <span class="name">HARTWELL</span>
    <span class="golf">GOLF</span>
    <span class="year">DAY 2018</span>
  </h1>

  <div class="location">
    <span class="label">
      <svg width="14" height="20" viewBox="0 0 14 20" aria-hidden="true"><path d="M7 0a7 7 0 0 0-7 7c0 5 7 13 7 13s7-8 7-13a7 7 0 0 0-7-7z" fill="#f4c20c"/><circle cx="7" cy="7" r="2.6" fill="#fff"/></svg>LOCATION
    </span>
    <span class="venue">RIDGEVIEW GOLF CLUB</span>
  </div>

  <div class="start-band"><span>8.45AM ARRIVAL 9AM SHOT GUN START &nbsp;FOR 18 HOLE PLAYERS</span></div>

  <section class="sessions">
    <div class="session session--clinic">
      <h3>CLINIC:</h3>
      <p>11.30am to 12.30pm<br>with a Golf Pro for non-Golfers</p>
    </div>
    <div class="session session--lunch">
      <h3>POST GOLF LUNCH:</h3>
      <p>From 1pm in the Dining Room<br>Guest Speaker: TBA</p>
    </div>
  </section>

  <div class="golf-ball" role="img" aria-label="Photograph of a white golf ball resting on grass"></div>

  <div class="payment">
    <span class="label">PAYMENT:</span>
    <span class="link">
      <svg class="cursor" width="22" height="32" viewBox="0 0 22 32" aria-hidden="true"><path d="M1 1v26l7-6 5 10 4-2-5-10h9z" fill="#fff" stroke="#0c0c0c" stroke-width="1.5"/></svg>
      www.hartwellgolfday.org
    </span>
  </div>
  <div class="pricing">PRICING: TBA</div>

  <div class="function-band">A combined Hartwell Old Scholars and Parents &amp; Friends Function</div>
</main>
</body>
</html>
```